Bramwell HVAC Service LLC Business Card

We just got a design created by one of your designers for a logo and now would like help with a business card design. The information to be included on the card is as follows:
Bramwell HVAC Service LLC (I will attach logo design)
P.O. Box 482
Dunmore, CO 80634
(970) 347-6159
Lonnie Tadwick
I might include an e-mail address, but I'm not sure yet.
Target Market(s)
Customers needing service or repairs done on their heating and air conditioning systems.
Industry/Entity Type
Business
Contact Information for Business Card
P.O. Box 482
Dunmore, CO 80634
(970) 347-6159
Lonnie Tadwick

```html
<!DOCTYPE html>
<html lang="en">
<head>
<meta charset="utf-8">
<title>Bramwell HVAC Service LLC – Business Card</title>
<link href="https://fonts.googleapis.com/css2?family=Cinzel:wght@400;700&family=Cormorant+SC:wght@500;600&display=swap" rel="stylesheet">
<style>
  :root {
    --backdrop: #e6e4e0;
    --card: #ffffff;
    --card-shade: #eeeeef;
    --navy: #2c4d8f;
    --red: #d3232c;
    --ink: #4a4a52;
  }
  * { margin: 0; padding: 0; box-sizing: border-box; }
  html, body {
    width: 1200px; height: 600px; overflow: hidden;
    background: var(--backdrop);
  }
  .card {
    position: absolute; left: 150px; top: 85px;
    width: 900px; height: 430px;
    background: radial-gradient(ellipse at 45% 45%, var(--card) 40%, var(--card-shade) 100%);
    box-shadow: 0 8px 24px rgba(0,0,0,.18);
    overflow: hidden;
  }
  .brand {
    position: absolute; left: 62px; top: 72px;
    display: flex; align-items: center; gap: 16px;
  }
  .brand-dot {
    width: 58px; height: 58px; border-radius: 50%;
    background: var(--red); flex: none;
  }
  .brand-name {
    font-family: "Cinzel", serif; font-weight: 700;
    color: var(--navy); font-size: 30px; line-height: 1.05;
    letter-spacing: .5px;
  }
  .holder {
    position: absolute; right: 126px; top: 212px;
    font-family: "Cinzel", serif; font-weight: 700;
    color: var(--red); font-size: 22px; letter-spacing: 1px;
  }
  .divider {
    position: absolute; left: 162px; right: 108px; top: 275px;
    height: 1.5px; background: var(--navy);
  }
  .contact {
    position: absolute; left: 128px; top: 290px;
    list-style: none;
    font-family: "Cormorant SC", serif; font-weight: 600;
    color: var(--ink); font-size: 17px; letter-spacing: .5px;
  }
  .contact li { display: flex; align-items: center; gap: 10px; height: 26px; }
  .contact svg { width: 15px; height: 15px; flex: none; }
  .address {
    position: absolute; right: 118px; top: 296px;
    font-family: "Cormorant SC", serif; font-weight: 600;
    color: var(--ink); font-size: 17px; text-align: right;
    line-height: 26px; letter-spacing: .5px; font-style: normal;
  }
  .band { position: absolute; bottom: 0; }
  .band-blue { left: 0; width: 75%; height: 24px; background: var(--navy); }
  .band-red { left: 75%; right: 0; height: 40px; background: var(--red); }
</style>
</head>
<body>
  <section class="card">
    <div class="brand">
      <span class="brand-dot"></span>
      <div class="brand-name">Bramwell HVAC<br>Service LLC</div>
    </div>

    <h1 class="holder">Lonnie Tadwick</h1>
    <div class="divider"></div>

    <ul class="contact">
      <li>
        <svg viewBox="0 0 16 16" aria-hidden="true">
          <rect width="16" height="16" rx="2" fill="#d3232c"/>
          <path d="M5 3.5l1.6 2.2-1 1.1c.6 1.4 1.6 2.4 3 3l1.1-1 2.2 1.6-.9 1.9C7 12 4 9 3.6 5z" fill="#fff"/>
        </svg>
        (970) 347-6159
      </li>
      <li>
        <svg viewBox="0 0 16 16" aria-hidden="true">
          <rect width="16" height="16" rx="2" fill="#d3232c"/>
          <rect x="3" y="4.5" width="10" height="7" fill="none" stroke="#fff" stroke-width="1.2"/>
          <path d="M3 4.5l5 4 5-4" fill="none" stroke="#fff" stroke-width="1.2"/>
        </svg>
        office@bramwellhvac.co
      </li>
    </ul>

    <address class="address">
      P.O. Box 482<br>
      Dunmore, CO 80634
    </address>

    <div class="band band-blue"></div>
    <div class="band band-red"></div>
  </section>
</body>
</html>
```